Redesign existing website

We would like a redesign of the website http://www.velbrisanalytics.com that creates a more modern, up to date look.

Velbris Analytics creates software for social science research and is focused on making the software user friendly and easy to use. We would like to convey seriousness, but also
a very up to date, just released look.

Feel free to modify the logo if you wish.

Target Market(s)

Academics, researchers

Industry/Entity Type

Software

Requirements
Must have
• The design should incorporate the same information as the current website.

```html
<!DOCTYPE html>
<html lang="en">
<head>
<meta charset="utf-8">
<title>Velbris Analytics</title>
<link rel="stylesheet" href="https://fonts.googleapis.com/css2?family=Fira+Sans+Condensed:ital,wght@0,400;0,600;0,700;1,600;1,700&family=Arimo:wght@400;700&display=swap">
<style>
:root{
  --blue-deep:#1a3f8f;
  --blue:#2a56b0;
  --navy-text:#1e3f8a;
  --page:#eeeff1;
  --band:#d9dbdf;
  --panel:#ffffff;
  --body-text:#8a8a8a;
  --dark:#222;
  --line:#d6d6d6;
}
*{box-sizing:border-box;margin:0;padding:0}
html,body{width:1200px;height:1003px;overflow:hidden}
body{position:relative;background:var(--page);font-family:"Arimo",Arial,sans-serif;color:var(--dark)}
.sky{position:absolute;left:0;top:0;width:1200px;height:250px;background:linear-gradient(180deg,#163a86 0%,#2c5bb4 70%,#3a68bd 100%)}
.ground{position:absolute;left:0;top:874px;width:1200px;height:129px;background:var(--band)}
.header{position:absolute;left:180px;top:0;width:854px;height:106px}
.brand-shape{position:absolute;left:0;top:0}
.brand{position:absolute;left:14px;top:0;width:180px;height:106px;display:flex;align-items:center;justify-content:center;gap:8px}
.brand-dot{width:16px;height:16px;border-radius:50%;background:var(--blue-deep)}
.brand-name{font-family:"Fira Sans Condensed",sans-serif;font-weight:600;font-size:20px;color:var(--blue-deep)}
.tagline{position:absolute;right:14px;top:26px;font-family:"Fira Sans Condensed",sans-serif;font-style:italic;font-weight:700;font-size:18px;color:#fff;white-space:nowrap}
.nav{position:absolute;left:180px;top:72px;width:854px;height:34px;background:linear-gradient(#f4f4f4,#d8d8d8);display:flex;list-style:none;padding-left:372px}
.nav li{font-weight:700;font-size:13px;color:#222;line-height:34px;padding:0 21px}
.nav li.active{background:var(--blue);color:#fff;border-radius:6px 6px 0 0;margin-top:2px;line-height:32px;padding:0 18px}
.hero{position:absolute;left:180px;top:106px;width:854px;height:246px;background:radial-gradient(ellipse at 45% 100%,#5e8fda 0%,#2e5fb8 45%,#1f4aa0 100%);overflow:hidden}
.hero-shot{position:absolute;left:77px;top:35px;width:223px;height:186px;background:linear-gradient(#e8eef7,#b8c8e0);box-shadow:6px 6px 14px rgba(0,0,0,.35)}
.hero-copy{position:absolute;left:429px;top:40px;color:#fff;font-family:"Fira Sans Condensed",sans-serif;font-style:italic}
.hero-copy h1{font-size:40px;font-weight:700;line-height:1}
.hero-copy h2{font-size:30px;font-weight:600;line-height:1.1;margin:8px 0 0 4px}
.hero-copy p{font-size:10.5px;font-weight:600;line-height:1.6;margin-top:14px;width:400px}
.read-more{position:absolute;left:742px;top:334px;width:115px;height:38px;background:linear-gradient(#fff,#dcdcdc);border-radius:6px 6px 0 0;font-family:"Fira Sans Condensed",sans-serif;font-weight:700;font-size:19px;color:#222;text-align:center;line-height:40px;box-shadow:0 -2px 4px rgba(0,0,0,.15)}
.panel{position:absolute;left:180px;top:400px;width:854px;height:551px;background:var(--panel);border-radius:8px;box-shadow:0 2px 8px rgba(0,0,0,.12)}
.features{position:absolute;left:0;top:37px;width:854px;display:flex}
.feature{flex:1;text-align:center}
.feature h3{font-family:"Fira Sans Condensed",sans-serif;font-weight:600;font-size:17px;color:#111;display:flex;align-items:center;justify-content:center;gap:8px}
.feature h3 svg{flex:none}
.thumb{margin:16px auto 0;width:112px;height:76px}
.thumb.screen{background:linear-gradient(#e9eff8,#b7c7df)}
.thumb.flow{background:linear-gradient(#f3d9a6,#c9cfdc)}
.thumb.chart{background:linear-gradient(#f2c871,#9cb4d8)}
.rule{position:absolute;left:60px;width:734px;height:1px;background:var(--line)}
.mission{position:absolute;left:0;top:193px;width:854px;text-align:center;font-family:"Fira Sans Condensed",sans-serif;font-style:italic;font-weight:600;font-size:12px;letter-spacing:-.1px;line-height:24px;color:#b5b5b5;white-space:nowrap}
.slogan{position:absolute;left:20px;top:290px;width:190px;text-align:center;font-size:33px;line-height:51px;color:#a6a6a6}
.family{position:absolute;left:235px;top:308px;font-family:"Fira Sans Condensed",sans-serif;font-weight:600;font-size:16px;color:var(--navy-text)}
.portrait{position:absolute;left:235px;top:346px;width:96px;height:120px;background:linear-gradient(#9d8f84,#5c5048);border:1px solid #ccc}
.bio{position:absolute;left:360px;top:344px;width:220px}
.bio h4{font-family:"Fira Sans Condensed",sans-serif;font-weight:600;font-size:14px;color:#333}
.bio p{margin-top:10px;font-size:11px;line-height:18px;color:var(--body-text);height:108px;overflow:hidden}
.preview{position:absolute;left:622px;top:291px;width:206px;height:197px;border-radius:12px;overflow:hidden;background:linear-gradient(#f8f8f8,#d6d6d6);box-shadow:0 2px 6px rgba(0,0,0,.25);text-align:center;font-family:"Fira Sans Condensed",sans-serif;font-style:italic}
.preview .kicker{margin-top:16px;font-weight:700;font-size:15px;color:#111}
.preview .product{margin-top:6px;font-weight:700;font-size:37px;line-height:40px;color:#111}
.preview .download{position:absolute;left:0;bottom:0;width:100%;height:48px;background:var(--blue-deep);color:#fff;font-weight:600;font-size:13px;line-height:48px}
.footer{position:absolute;left:192px;top:967px;font-size:12.5px;color:#333}
.social{position:absolute;left:948px;top:965px;display:flex;gap:7px}
.social span{width:14px;height:14px;border-radius:2px}
</style>
</head>
<body>
<div class="sky"></div>
<div class="ground"></div>

<header class="header">
  <svg class="brand-shape" width="240" height="106" viewBox="0 0 240 106" aria-hidden="true"><path d="M0 0H150C200 0 230 30 236 72V106H0Z" fill="#fff"/></svg>
  <div class="brand"><span class="brand-dot"></span><span class="brand-name">Velbris Analytics</span></div>
  <p class="tagline">Increasing the power and efficiency of empirical social science research</p>
</header>
<ul class="nav">
  <li class="active">Home</li><li>Products</li><li>News</li><li>About Us</li><li>Contact Us</li>
</ul>

<section class="hero">
  <div class="hero-shot" role="img" aria-label="Screenshot of the Tessera Data Manager application window"></div>
  <div class="hero-copy">
    <h1>Tessera Data Manager</h1>
    <h2>Social Science and<br>Health Data Management</h2>
    <p>The technology used for retrieving and manipulating data has remained virtually unchanged since the first statistical packages were introduced almost four decades ago</p>
  </div>
</section>
<div class="read-more">Read More</div>

<main class="panel">
  <div class="features">
    <div class="feature">
      <h3><svg width="16" height="18" viewBox="0 0 16 18"><ellipse cx="8" cy="3.5" rx="7" ry="3" fill="#888"/><path d="M1 3.5v11c0 1.7 3.1 3 7 3s7-1.3 7-3v-11c0 1.7-3.1 3-7 3s-7-1.3-7-3z" fill="#aaa"/></svg>Tessera Data Manager</h3>
      <div class="thumb screen" role="img" aria-label="Application screenshot"></div>
    </div>
    <div class="feature">
      <h3><svg width="18" height="16" viewBox="0 0 18 16"><rect x="1" y="1" width="16" height="14" rx="2" fill="#5b8fd6"/><rect x="3" y="3" width="12" height="8" fill="#cfe0f6"/></svg>Tessera Data Manager Process</h3>
      <div class="thumb flow" role="img" aria-label="Diagram of the data manager process"></div>
    </div>
    <div class="feature">
      <h3><svg width="18" height="16" viewBox="0 0 18 16"><rect x="1" y="6" width="4" height="10" fill="#d33"/><rect x="7" y="2" width="4" height="14" fill="#e88a2a"/><rect x="13" y="8" width="4" height="8" fill="#3a6fc4"/></svg>Data Restructuring</h3>
      <div class="thumb chart" role="img" aria-label="Illustration of data restructuring"></div>
    </div>
  </div>
  <div class="rule" style="top:179px"></div>
  <p class="mission">The mission of Velbris Analytics is to produce software products that multiply the power and efficiency of empirical scientific research in the social sciences.<br>A central goal is to expand access to complex data sources and to the advanced methods of scientific investigation needed to analyze them.</p>
  <div class="rule" style="top:256px"></div>

  <p class="slogan">Empowering the social science researcher</p>
  <h3 class="family">The Hartwell Family</h3>
  <div class="portrait" role="img" aria-label="Portrait photo of the president and CEO"></div>
  <div class="bio">
    <h4>Daniel Hartwell, President and CEO</h4>
    <p>Daniel Hartwell has compiled an impressive record of accomplishment in the realm of empirical social science research. Early on, Daniel realized that the ability to use the decennial U. S. censuses as a time series, linking across the years, would add historical depth to population and policy research. Such</p>
  </div>
  <div class="preview">
    <p class="kicker">Preview Release Available!</p>
    <p class="product">Tessera Data<br>Manager</p>
    <p class="download">Download Preview Release</p>
  </div>
</main>

<p class="footer">© 2011 All Rights Reserved.</p>
<div class="social" aria-label="Social links">
  <span style="background:#3b5998"></span><span style="background:#4ab3e8"></span><span style="background:#f08a24"></span><span style="background:#8a8a8a"></span>
</div>
</body>
</html>
```